Land Buying Company Needs Letterhead for Direct Mail Marketing to Land Owners

We are looking for a professional letterhead that we will be including in our direct mail marketing. We will be sending this to land owners who may be interested in selling or purchasing land.

The letterhead needs to be editable. Headers and footers would look nice, but we are open. We would want it to include our address, website, phone, and email info. For right now the address to use for design purposes would the following:

Address: 415 Bramwell Avenue #600
Dallas, TX 75219
Website - www.quillridgeacres.example
Email - info@quillridgeacres.example
Phone - 866-402-ACRE

I have attached our logo zip file that we just had done on Pixel Guild. Let me know what questions you have, and thank you.

```html
<!DOCTYPE html>
<html lang="en">
<head>
<meta charset="utf-8">
<title>Quillridge Acres Letterhead</title>
<link rel="stylesheet" href="https://fonts.googleapis.com/css2?family=Roboto:wght@400;500&display=swap">
<style>
  :root {
    --green-light: #8dc63f;
    --green-dark: #3d5a1f;
    --ink: #1c1c1c;
    --rule: #4a6a26;
    --paper: #ffffff;
    --backdrop: #ececec;
  }
  * { box-sizing: border-box; margin: 0; padding: 0; }
  html, body {
    width: 1200px; height: 1200px; overflow: hidden;
    background: var(--backdrop);
    font-family: "Roboto", Arial, sans-serif;
    color: var(--ink);
  }
  .letterhead {
    position: absolute; left: 190px; top: 70px;
    width: 820px; height: 1060px;
    background: var(--paper);
    overflow: hidden;
  }
  .brand {
    position: absolute; left: 62px; top: 92px;
    display: flex; align-items: center; gap: 16px;
  }
  .brand-dot {
    width: 62px; height: 62px; border-radius: 50%;
    background: var(--green-dark);
  }
  .brand-name {
    font-size: 38px; font-weight: 500; letter-spacing: 1px;
    color: var(--green-light); text-transform: uppercase;
  }
  .contact {
    position: absolute; left: 506px; top: 62px;
    list-style: none; font-size: 11.5px;
  }
  .contact li {
    display: flex; align-items: center; gap: 14px;
    height: 26px;
  }
  .contact svg { width: 14px; height: 14px; flex: none; }
  .header-rule {
    position: absolute; left: 62px; right: 38px; top: 154px;
    border-top: 1.5px solid var(--rule);
  }
  .date {
    position: absolute; left: 530px; top: 164px;
    font-size: 11px;
  }
  .body {
    position: absolute; left: 96px; right: 92px; top: 218px;
    font-size: 14.5px; line-height: 21px;
  }
  .salutation { margin-bottom: 34px; }
  .body p.para { text-align: justify; margin-bottom: 20px; }
  .closing {
    position: absolute; left: 130px; top: 880px;
    font-size: 14.5px;
  }
  .footer-wave {
    position: absolute; left: 0; bottom: 0;
    width: 820px; height: 180px;
  }
  .address {
    position: absolute; right: 52px; bottom: 40px;
    font-size: 12.5px; color: var(--ink);
  }
</style>
</head>
<body>
  <main class="letterhead">
    <header>
      <div class="brand">
        <span class="brand-dot"></span>
        <span class="brand-name">Quillridge Acres</span>
      </div>
      <ul class="contact">
        <li>
          <svg viewBox="0 0 14 14"><circle cx="7" cy="7" r="7" fill="var(--green-light)"/><rect x="3.5" y="4.5" width="7" height="5" fill="none" stroke="#fff" stroke-width="1"/><path d="M3.5 4.5 L7 7.5 L10.5 4.5" fill="none" stroke="#fff" stroke-width="1"/></svg>
          info@quillridgeacres.example
        </li>
        <li>
          <svg viewBox="0 0 14 14"><circle cx="7" cy="7" r="7" fill="var(--green-light)"/><circle cx="7" cy="7" r="3.6" fill="none" stroke="#fff" stroke-width="1"/><path d="M3.4 7 H10.6 M7 3.4 V10.6" stroke="#fff" stroke-width="0.8"/></svg>
          www.quillridgeacres.example
        </li>
        <li>
          <svg viewBox="0 0 14 14"><circle cx="7" cy="7" r="7" fill="var(--green-light)"/><path d="M4.6 4 L6 4 L6.6 5.8 L5.8 6.5 Q6.5 8 7.6 8.4 L8.3 7.6 L10 8.2 L10 9.6 Q6.8 10.3 4.4 5.6 Z" fill="#fff"/></svg>
          866-402-ACRE
        </li>
      </ul>
      <div class="header-rule"></div>
      <p class="date">Date.........</p>
    </header>

    <section class="body">
      <p class="salutation">Dear Sir</p>
      <p class="para">Lorem ipsum dolor sit amet, consectetur adipiscing elit. Nunc eu dignissim eros. Donec mollis nunc id tellus venenatis venenatis. Nullam consequat semper tellus nec sagittis. Quisque sit amet sodales ex, a mollis urna. Praesent at sodales elit. Proin vel cursus orci. Vivamus posuere velit vel diam accumsan faucibus.</p>
      <p class="para">Integer id purus at eros facilisis pellentesque. Nam in posuere libero. Pellentesque habitant morbi tristique senectus et netus et malesuada fames ac turpis egestas. Integer sagittis consectetur odio, at tristique nunc mattis sed. Morbi ac fringilla nunc, at posuere sem. Etiam mauris tortor, mollis nec dolor eu, consectetur convallis mauris. Donec euismod auctor mi, at sodales velit pretium nec. Integer ultricies lacus id pharetra aliquet.</p>
      <p class="para">Nulla viverra hendrerit tortor ac placerat. Fusce sed pulvinar sem. Suspendisse diam metus, varius rutrum nisi et, scelerisque pellentesque lacus. Fusce rutrum sem magna, non maximus elit placerat eu. In facilisis nulla ac nisl sodales, eu ullamcorper enim posuere. Mauris placerat urna quis felis dignissim pretium. Nulla nec interdum elit, pellentesque eleifend dui. Pellentesque aliquet gravida metus, in vestibulum orci commodo in. Aenean ut interdum dui. Aliquam dignissim arcu vel nulla blandit, vitae pellentesque urna condimentum. Pellentesque elementum nec eros vitae sagittis. Integer iaculis nibh non laoreet suscipit.</p>
      <p class="para">Maecenas interdum ante sed nisi varius tincidunt. Cras fermentum eu purus eget luctus. Mauris ac diam nec urna ullamcorper porttitor in quis quam. Maecenas congue nulla ornare, commodo tellus consequat, viverra nunc. Integer faucibus quam eget lorem suscipit lacinia quis at dolor. Interdum et malesuada fames ac ante ipsum primis in faucibus. Aenean ornare diam sit amet lectus ultrices, vel molestie dolor congue. Etiam sem neque, dapibus ut massa sit amet, convallis accumsan lectus. Class aptent taciti sociosqu ad litora torquent per conubia nostra, per inceptos himenaeos. Maecenas lobortis ipsum ut purus vulputate varius. Aliquam in vehicula risus.</p>
    </section>

    <p class="closing">Regards</p>

    <footer>
      <svg class="footer-wave" viewBox="0 0 820 180" preserveAspectRatio="none">
        <path d="M0 150 C200 150 380 120 520 72 C620 38 720 20 820 30 L820 180 L0 180 Z" fill="var(--green-light)"/>
        <path d="M0 112 C150 128 300 128 420 100 C300 140 150 145 0 132 Z" fill="var(--green-dark)"/>
      </svg>
      <p class="address">Address: 415 Bramwell Avenue #600, Dallas, TX 75219</p>
    </footer>
  </main>
</body>
</html>
```